Flyer-Design für Wechseljahresberatung
Zielgruppe
Zielgruppe: überwiegend Frauen
psycholog. Beratung in allen Lebenslagen, Wechseljahresberatung , Gesundheits- und Ernährungsberatung, Fastenbegleitung, Trauerbegleitung, Bachblütenberatung,Klangmassagen
Aufgabenstellung
es geht um einen 6teiligen Kurs für Frauen zwischen Ende 30 bis Ende 60. Beginn der Wechseljahre , Leben in den Wechseljahren und was kommt danach? Wie erkennt man (Frau) körperl. oder seelische Probleme, die schon auf We.jahre hindeuten? Wie gehe Frau damit um? Was passiert in den We.jahren? Was kann Frau selbst tun, um die We.jahre so gut wie möglich zu erleben? Im Kurs werden natürliche Hilfsmittel besprochen und erklärt, Entspannungstechniken vermittelt , die Psyche gestärkt, sodaß die betroffenen Frauen bei auftretenden We.jahrsproblemen die Möglichkeit haben,sich selbst helfen zu können.

```html
<!DOCTYPE html>
<html lang="de">
<head>
<meta charset="utf-8">
<title>Flyer Wechseljahre – Beratung und Begleitung</title>
<link rel="stylesheet" href="https://fonts.googleapis.com/css2?family=Patrick+Hand&family=Fira+Sans:wght@300;400;500&display=swap">
<style>
:root{
  --red:#cc2e50;
  --yellow:#fbe58b;
  --cream:#fff1b8;
  --blue:#5b93c9;
  --green:#8cbf2a;
  --grey-box:#dedede;
  --ink:#2a2a2a;
  --white:#ffffff;
  --stage:#d3d3d3;
  --hand:"Patrick Hand", cursive;
  --sans:"Fira Sans", sans-serif;
}
*{margin:0;padding:0;box-sizing:border-box}
html,body{width:1200px;height:3513px;overflow:hidden;background:var(--white)}
body{position:relative;font-family:var(--sans);color:var(--ink)}

.stage{position:absolute;left:28px;top:28px;width:1144px;height:991px;
  background:radial-gradient(ellipse at 50% 40%,#f1f1f1 0%,var(--stage) 100%)}
.stage .cover-flat{position:absolute;left:349px;top:23px;width:572px;height:1211px;
  transform:scale(.78);transform-origin:0 0;box-shadow:0 10px 30px rgba(0,0,0,.25)}

.spread{position:absolute;left:28px;width:1144px;height:1211px;background:var(--white);
  box-shadow:0 1px 4px rgba(0,0,0,.15);overflow:hidden}
.spread-outside{top:1047px}
.spread-inside{top:2283px}
.spread-bg{position:absolute;left:0;top:0}

/* cover */
.cover-text{position:absolute;left:38px;top:30px;width:520px;font-family:var(--hand)}
.cover-title{color:var(--yellow);font-size:62px;line-height:1;letter-spacing:2px;font-weight:400}
.cover-sub{color:var(--yellow);font-size:31px;letter-spacing:1.5px;line-height:1.1;margin-bottom:14px}
.cover-topics{list-style:none;color:var(--cream);font-size:29px;line-height:38px;letter-spacing:.5px}
.motto{position:absolute;font-family:var(--hand);color:var(--white);font-size:37px;line-height:64px;text-align:center;letter-spacing:1px}

/* outside left panel */
.adviser{position:absolute;left:39px;top:30px}
.adviser-name{font-size:31px;font-weight:400}
.adviser-title{font-size:21px;font-weight:300;line-height:28px;color:#444}
.photo-slot{position:absolute;left:39px;top:150px;width:484px;height:257px;background:#eef1f8}
.services{position:absolute;left:39px;top:440px;list-style:none;color:var(--red);font-size:24px;line-height:74px;font-weight:300}
.services li::before{content:"• ";font-size:20px}
.brand{position:absolute;left:36px;top:1052px;display:flex;align-items:center;gap:10px;color:var(--white);font-size:22px;font-weight:400;letter-spacing:2px}
.brand-dot{width:18px;height:18px;border-radius:50%;background:var(--white)}
.contact{position:absolute;left:204px;top:1030px;color:var(--white);font-size:16.5px;line-height:20.5px;font-weight:300;font-style:normal}
.contact .gap{height:14px}
.contact span{display:inline-block;width:64px}
.contact strong{font-weight:400}

/* inside */
.inside-title{position:absolute;left:45px;top:30px;color:var(--white);font-size:31px;font-weight:300}
.col{position:absolute;font-size:19px;line-height:27px;font-weight:300;text-align:justify;hyphens:manual;letter-spacing:-.1px}
.col p{margin-bottom:27px}
.col-left{left:45px;top:136px;width:485px}
.col-right{left:608px;top:445px;width:491px}
.topics{list-style:none;margin-bottom:27px;text-align:left}
.topics li{padding-left:13px;text-indent:-13px}
.topics li::before{content:"• "}
.course-box{position:absolute;left:608px;top:91px;width:491px;height:314px;background:var(--grey-box);padding:22px 24px;font-size:20px;line-height:26px;font-weight:300}
.course-box h2{font-size:31px;font-weight:400;margin-bottom:16px}
.course-box dt{font-weight:500;margin-top:22px}
.forest-caption{position:absolute;left:610px;top:1112px;width:500px;text-align:center;font-family:var(--hand);color:var(--white);font-size:32px;line-height:34px;letter-spacing:1.5px}
</style>
</head>
<body>

<section class="stage" aria-label="Präsentation">
  <div class="cover-flat spread">
    <svg class="spread-bg" width="572" height="1211" viewBox="0 0 572 1211">
      <defs>
        <radialGradient id="meadowA" cx="60%" cy="40%" r="70%">
          <stop offset="0" stop-color="#f3f6c8"/><stop offset=".45" stop-color="#b6cf6a"/><stop offset="1" stop-color="#5f8f2c"/>
        </radialGradient>
      </defs>
      <path d="M0,0H572V312C420,300 200,330 0,350Z" fill="var(--red)"/>
      <path d="M0,350C200,330 420,300 572,312V330C420,318 200,348 0,368Z" fill="var(--yellow)"/>
      <path d="M0,960C200,935 400,910 572,890V1211H0Z" fill="var(--blue)"/>
      <path role="img" aria-label="Foto: Frau in blauer Strickjacke sitzt im sonnigen Gras im Wald" d="M0,374C200,354 420,324 572,336V870C400,895 200,920 0,942Z" fill="url(#meadowA)"/>
    </svg>
    <div class="cover-text">
      <h1 class="cover-title">WECHSELJAHRE</h1>
      <p class="cover-sub">BERATUNG UND BEGLEITUNG</p>
      <ul class="cover-topics">
        <li>Möglichkeiten zur Selbsthilfe</li>
        <li>Vorbereitung auf die Wechseljahre</li>
        <li>Leben in den Wechseljahren</li>
        <li>Was kommt danach?</li>
      </ul>
    </div>
    <p class="motto" style="left:36px;top:980px;width:500px">Alles hat nur die<br>Bedeutung, die man<br>ihr gibt.</p>
  </div>
</section>

<section class="spread spread-outside" aria-label="Außenseite">
  <svg class="spread-bg" width="1144" height="1211" viewBox="0 0 1144 1211">
    <defs>
      <radialGradient id="meadowB" cx="60%" cy="40%" r="70%">
        <stop offset="0" stop-color="#f3f6c8"/><stop offset=".45" stop-color="#b6cf6a"/><stop offset="1" stop-color="#5f8f2c"/>
      </radialGradient>
    </defs>
    <path d="M572,0H1144V312C992,300 772,330 572,350Z" fill="var(--red)"/>
    <path d="M572,350C772,330 992,300 1144,312V330C992,318 772,348 572,368Z" fill="var(--yellow)"/>
    <path d="M0,962C320,990 700,930 1144,890V1211H0Z" fill="var(--blue)"/>
    <path role="img" aria-label="Foto: Frau in blauer Strickjacke sitzt im sonnigen Gras im Wald" d="M572,374C772,354 992,324 1144,336V876C950,900 760,925 572,945Z" fill="url(#meadowB)"/>
  </svg>

  <div class="adviser">
    <p class="adviser-name">Marlene Vogt-Hansen</p>
    <p class="adviser-title">Wechseljahre-Beraterin (zert.)<br>Systemische Beratung (zert.)</p>
  </div>
  <div class="photo-slot"></div>
  <ul class="services">
    <li>Psycholog. Beratung in allen Lebenslagen</li>
    <li>Wechseljahresberatung</li>
    <li>Gesundheits- und Ernährungsberatung</li>
    <li>Fastenbegleitung</li>
    <li>Trauerbegleitung</li>
    <li>Bachblütenberatung</li>
    <li>Klangmassagen</li>
  </ul>

  <div class="cover-text" style="left:610px">
    <h1 class="cover-title">WECHSELJAHRE</h1>
    <p class="cover-sub">BERATUNG UND BEGLEITUNG</p>
    <ul class="cover-topics">
      <li>Möglichkeiten zur Selbsthilfe</li>
      <li>Vorbereitung auf die Wechseljahre</li>
      <li>Leben in den Wechseljahren</li>
      <li>Was kommt danach?</li>
    </ul>
  </div>

  <div class="brand"><span class="brand-dot"></span>LUNARA</div>
  <address class="contact">
    <strong>Lunara</strong><br>
    Marlene Vogt-Hansen<br>
    Lindenweg 12<br>
    6411AB Heerlen / NL
    <div class="gap"></div>
    <span>Telefon:</span>0241 / 00 00 00 00<br>
    <span>oder</span>+31(0)45/ 0 00 00 00<br>
    <span>Mail:</span>mondhalmkreise@postfach.example
  </address>

  <p class="motto" style="left:610px;top:978px;width:500px">Alles hat nur die<br>Bedeutung, die man<br>ihr gibt.</p>
</section>

<section class="spread spread-inside" aria-label="Innenseite">
  <svg class="spread-bg" width="1144" height="1211" viewBox="0 0 1144 1211">
    <defs>
      <radialGradient id="forest" cx="74%" cy="20%" r="80%">
        <stop offset="0" stop-color="#fff9c4"/><stop offset=".18" stop-color="#d9e66a"/><stop offset=".5" stop-color="#6f9a2e"/><stop offset="1" stop-color="#2f5a1c"/>
      </radialGradient>
    </defs>
    <path d="M0,0H1144V20C900,28 560,60 300,86C170,98 70,100 0,98Z" fill="var(--red)"/>
    <path d="M0,896C300,868 700,870 1144,816V830C700,884 300,882 0,910Z" fill="var(--green)"/>
    <path role="img" aria-label="Foto: sonnendurchfluteter grüner Laubwald" d="M0,914C300,886 700,888 1144,834V1211H0Z" fill="url(#forest)"/>
  </svg>

  <h2 class="inside-title">Kursangebot Wechseljahre</h2>

  <div class="col col-left">
    <p>Im Alter zwischen ca. 30 und 60 Jahren stellt sich der weibliche Körper hormonell um.</p>
    <p>Frauen erleben diese körperlichen und auch psychi&shy;schen Veränderungen in sehr unterschiedlicher Dauer und Intensität - dabei entstehen viele Fragen und der Wunsch nach Unterstützung.<br>So individuell ihre Symptome sind, so vielfältig sind auch die Lösungen.</p>
    <p>Im 6-teiligen Kurs für Frauen geht es unter anderem um:</p>
    <ul class="topics">
      <li>Beginn der Wechseljahre</li>
      <li>Leben in den Wechseljahren</li>
      <li>Was kommt danach?</li>
      <li>Wie werden seelische Probleme erkannt?</li>
      <li>Was passiert in den Wechseljahren?</li>
      <li>Was kann Frau tun, um die Wechseljahre<br>so gut wie möglich zu erleben?</li>
    </ul>
    <p>Im Kurs werden natürliche Hilfsmittel besprochen und erklärt, Entspannungstechniken vermittelt, die Psyche gestärkt, sodaß die betroffenen Frauen bei aufreten&shy;den Wechseljahresproblemen die Möglichkeit haben, sich selbst helfen zu können.</p>
  </div>

  <div class="course-box">
    <h2>Start Kurs 2017</h2>
    <p>02. September<br>6 x Samstags 14:00 - 16:00 Uhr</p>
    <dl>
      <dt>Kursbeitrag</dt><dd>160,- pro Teilnehmerin (6x2 Std.)</dd>
      <dt>Kursort</dt><dd>Lunara Heerlen</dd>
    </dl>
  </div>

  <div class="col col-right">
    <p>Die Wechseljahre bringen körperliche Veränderungen mit sich, die uns verunsichern. Gleichzeitig erleben auch viele von uns Einschnitte in ihren Beziehungen oder es fehlt der Sinn im Arbeitsleben.</p>
    <p>Wir stellen uns Fragen, die wir uns bisher nicht getraut haben zu stellen: "Was will ich eigentlich, was möchte ich mit meinem Leben noch anfangen?" Vielleicht wollen wir das Alte nicht mehr, aber wagen auch noch nicht den Schritt ins Neue.</p>
    <p style="text-align:left">In solchen Zeiten ist es wichtig, unsere Aufmerksamkeit auf uns selbst und nach Innen zu richten.</p>
  </div>

  <p class="forest-caption">Aufmerksamkeit auf sich selbst<br>und nach Innen</p>
</section>

</body>
</html>
```